New modern business card design

To design a brand new business card that's clean & modern in terms of layout.
I have attached our company logo and also basic information regarding what is needed on the card that also needs to be editable.

Target Market(s)

motor trade

Contact Information for Business Card

logo, name, title, tel, mob, email, address, www, all information is in the word.doc file

Requirements
Must have
• white background
Nice to have
• Nice clean font

```html
<!DOCTYPE html>
<html lang="en">
<head>
<meta charset="utf-8">
<title>Kestrel Extract Ltd — Business Card</title>
<link href="https://fonts.googleapis.com/css2?family=Jost:wght@500;600&display=swap" rel="stylesheet">
<style>
  :root {
    --stage: #dedbda;
    --card: #ffffff;
    --card-shade: #f1f1f2;
    --brand-blue: #2a6fbd;
    --panel-blue: #5592cc;
    --panel-blue-deep: #4a86c2;
    --accent-grey: #a7a7a7;
    --ink: #2b2326;
    --white: #ffffff;
  }
  * { margin: 0; padding: 0; box-sizing: border-box; }
  html, body { width: 1200px; height: 1200px; overflow: hidden; }
  body {
    background: var(--stage);
    font-family: "Jost", "Helvetica Neue", Arial, sans-serif;
    position: relative;
  }
  .card {
    position: absolute;
    left: 179px;
    width: 840px;
    height: 480px;
    background: linear-gradient(135deg, var(--card) 0%, var(--card-shade) 45%, var(--card) 70%, var(--card-shade) 100%);
    box-shadow: 2px 3px 4px rgba(0,0,0,0.35);
    overflow: hidden;
  }
  .card--front { top: 99px; }
  .card--back { top: 627px; }
  .panel {
    position: absolute;
    top: 92px;
    height: 295px;
    background: linear-gradient(160deg, var(--panel-blue-deep) 0%, var(--panel-blue) 50%, var(--panel-blue-deep) 100%);
  }
  .rule {
    position: absolute;
    top: 92px;
    width: 8px;
    height: 295px;
    background: var(--panel-blue-deep);
  }
  .accent-square {
    position: absolute;
    width: 47px;
    height: 47px;
    background: var(--accent-grey);
  }
  .accent-square--blue { background: var(--brand-blue); }
  .line { position: absolute; white-space: nowrap; line-height: 1; }

  .holder-name { left: 55px; top: 219px; font-size: 41px; font-weight: 600; color: var(--white); letter-spacing: 0.3px; }
  .holder-role { right: 445px; top: 263px; font-size: 23px; font-weight: 600; color: var(--white); }

  .wordmark { color: var(--brand-blue); font-weight: 500; text-align: center; line-height: 1.15; letter-spacing: 1px; }
  .wordmark--small { position: absolute; left: 598px; top: 58px; width: 195px; font-size: 18px; }
  .wordmark--large { position: absolute; left: 20px; top: 200px; width: 345px; font-size: 36px; }

  .contact-icon { position: absolute; left: 472px; width: 34px; height: 34px; }
  .contact-text { left: 525px; color: var(--ink); font-weight: 500; }
  .contact-text--phone { font-size: 22px; }
  .contact-text--small { font-size: 21px; }

  .web { font-size: 29px; font-weight: 600; color: var(--brand-blue); }
  .tagline { left: 406px; top: 231px; font-size: 28px; font-weight: 600; color: var(--white); word-spacing: 4px; }
</style>
</head>
<body>

<section class="card card--front" aria-label="Business card front">
  <div class="panel" style="left:0; width:443px;"></div>
  <div class="rule" style="left:453px;"></div>
  <div class="accent-square" style="left:0; top:216px;"></div>
  <div class="accent-square accent-square--blue" style="left:793px; top:51px;"></div>

  <div class="wordmark wordmark--small">KESTREL EXTRACT<br>LTD</div>

  <p class="line holder-name">DANIEL HARTLEY</p>
  <p class="line holder-role">General Manager</p>

  <svg class="contact-icon" style="top:137px;" viewBox="0 0 34 34" aria-hidden="true">
    <circle cx="17" cy="17" r="17" fill="var(--brand-blue)"/>
    <rect x="9" y="9" width="16" height="16" rx="3" fill="none" stroke="#fff" stroke-width="2"/>
    <path d="M13 12c0 5 4 9 9 9l1-2-3-1-1 1c-2-1-3-2-4-4l1-1-1-3z" fill="#fff"/>
  </svg>
  <p class="line contact-text contact-text--phone" style="top:145px;">0161 555 0142</p>

  <svg class="contact-icon" style="top:179px;" viewBox="0 0 34 34" aria-hidden="true">
    <circle cx="17" cy="17" r="17" fill="var(--brand-blue)"/>
    <rect x="12" y="8" width="10" height="18" rx="2" fill="none" stroke="#fff" stroke-width="2"/>
    <circle cx="17" cy="22.5" r="1.2" fill="#fff"/>
  </svg>
  <p class="line contact-text contact-text--phone" style="top:188px;">07700 900 418</p>

  <svg class="contact-icon" style="top:222px;" viewBox="0 0 34 34" aria-hidden="true">
    <circle cx="17" cy="17" r="17" fill="var(--brand-blue)"/>
    <rect x="9" y="11" width="16" height="12" rx="1.5" fill="#fff"/>
    <path d="M9.5 12l7.5 6 7.5-6" fill="none" stroke="var(--brand-blue)" stroke-width="1.8"/>
  </svg>
  <p class="line contact-text contact-text--small" style="top:233px;">dhartley@kestrel-extract.co.uk</p>

  <svg class="contact-icon" style="top:265px;" viewBox="0 0 34 34" aria-hidden="true">
    <circle cx="17" cy="17" r="17" fill="var(--brand-blue)"/>
    <path d="M17 25c-4-5-6-8-6-11a6 6 0 0 1 12 0c0 3-2 6-6 11z" fill="none" stroke="#fff" stroke-width="2"/>
    <circle cx="17" cy="14" r="2" fill="#fff"/>
  </svg>
  <p class="line contact-text contact-text--small" style="top:276px;">Mill Lane</p>
  <p class="line contact-text contact-text--small" style="top:301px;">Ashbrook, Manchester</p>
  <p class="line contact-text contact-text--small" style="top:328px;">M99 2QX</p>

  <p class="line web" style="left:67px; top:416px;">www.kestrel-extract.co.uk</p>
</section>

<section class="card card--back" aria-label="Business card back">
  <div class="wordmark wordmark--large">KESTREL EXTRACT<br>LTD</div>

  <div class="rule" style="left:378px;"></div>
  <div class="panel" style="left:396px; width:444px;"></div>
  <div class="accent-square" style="left:793px; top:215px;"></div>

  <p class="line tagline">YOUR TAGLINE GOES HERE</p>

  <p class="line web" style="left:442px; top:418px;">www.kestrel-extract.co.uk</p>
</section>

</body>
</html>
```